A Book Cover For a Book Called "Lantern"

Attached are two files for the ISBN bar graph for the print version of the cover! Same image, just two different formats.
Updates

Target Market(s)

young adult female, parents

Colors

```html
<!DOCTYPE html>
<html lang="en">
<head>
<meta charset="utf-8">
<title>Lantern — A Memoir</title>
<link rel="stylesheet" href="https://fonts.googleapis.com/css2?family=Alike&family=Josefin+Sans:wght@400&display=swap">
<style>
  :root {
    --bg-top: #1d1813;
    --bg-mid: #17130f;
    --bg-deep: #0f0c09;
    --title: #9c8160;
    --byline: #8d7b66;
    --subtitle: #a3978a;
    --satin-light: #cfc3b0;
    --satin-mid: #7e705f;
  }
  html, body {
    margin: 0;
    padding: 0;
    width: 818px;
    height: 1200px;
    overflow: hidden;
    background: var(--bg-deep);
  }
  .cover {
    position: relative;
    width: 818px;
    height: 1200px;
    overflow: hidden;
    background: linear-gradient(180deg, var(--bg-top) 0%, var(--bg-mid) 45%, var(--bg-deep) 100%);
  }
  .cover-photo {
    position: absolute;
    left: 0;
    right: 0;
    bottom: 0;
    height: 560px;
    background: radial-gradient(ellipse 70% 60% at 50% 88%, var(--satin-light) 0%, var(--satin-mid) 42%, rgba(23,19,15,0) 100%);
  }
  .title {
    position: absolute;
    top: 222px;
    left: 0;
    width: 818px;
    margin: 0;
    text-align: center;
    font-family: "Alike", serif;
    font-weight: 400;
    font-size: 88px;
    line-height: 1;
    letter-spacing: 0.28em;
    padding-left: 0.28em;
    box-sizing: border-box;
    color: var(--title);
  }
  .byline {
    position: absolute;
    top: 356px;
    left: 0;
    width: 818px;
    margin: 0;
    text-align: center;
    font-family: "Josefin Sans", sans-serif;
    font-size: 38px;
    line-height: 62px;
    letter-spacing: 0.16em;
    color: var(--byline);
  }
  .byline span { display: block; }
  .subtitle {
    position: absolute;
    top: 614px;
    left: 0;
    width: 818px;
    margin: 0;
    text-align: center;
    font-family: "Alike", serif;
    font-size: 34px;
    line-height: 1;
    letter-spacing: 0.2em;
    padding-left: 0.2em;
    box-sizing: border-box;
    color: var(--subtitle);
  }
</style>
</head>
<body>
  <main class="cover">
    <div class="cover-photo" role="img" aria-label="Close-up photograph of a pair of worn satin pointe shoes resting side by side in soft light"></div>
    <h1 class="title">LANTERN</h1>
    <p class="byline"><span>by Willow Hart</span><span>with Maren Cole</span></p>
    <p class="subtitle">A MEMOIR</p>
  </main>
</body>
</html>
```